Fully coded Word press template and New logo for Colocation Provider

We need a wordpress template and new logo for our website. The current website is rovelnhost.com. Rovel Host is a colocation provider located in San Antonio Texas. We are looking for a complete re-design of the site and logo. Everything is on the table. New colors, logo, look, feel...everything. Go wild! We are looking for a clean modern look.

P.S. The name Rovel originated from the Harrowmere Glen movies (Rovel is where the work was done).

Target Market(s)

We are targeting toward IT staffs and CFO's

Requirements
Must have
• Must have clean look. Although can have some playfulness too it, It must convey safety and security.

```html
<!DOCTYPE html>
<html lang="en">
<head>
<meta charset="utf-8">
<title>Rovel Host Services</title>
<link href="https://fonts.googleapis.com/css2?family=Open+Sans:wght@400;600;700&display=swap" rel="stylesheet">
<style>
  :root {
    --charcoal: #333333;
    --charcoal-dark: #2b2b2b;
    --green: #2db34a;
    --green-light: #3ec95a;
    --green-deep: #0f8a2a;
    --green-active: #0a7a22;
    --text: #333333;
    --rule: #555555;
    --card-border: #dddddd;
    --white: #ffffff;
    --footer-text: #e6e6e6;
  }
  * { box-sizing: border-box; margin: 0; padding: 0; }
  html, body { width: 1200px; height: 947px; overflow: hidden; background: var(--white); }
  body { position: relative; font-family: "Open Sans", Arial, sans-serif; color: var(--text); }

  .site-header { position: absolute; left: 0; top: 0; width: 1200px; height: 71px; background: var(--charcoal); }
  .brand { position: absolute; left: 143px; top: 19px; display: flex; align-items: center; gap: 8px;
    color: var(--green); font-size: 22px; font-weight: 700; letter-spacing: -0.3px; }
  .brand-mark { width: 22px; height: 22px; border-radius: 50%; background: var(--green); }

  .main-nav { position: absolute; left: 141px; top: 71px; width: 917px; height: 39px; display: flex; }
  .main-nav a { display: flex; align-items: center; justify-content: center; height: 100%;
    color: var(--white); text-decoration: none; font-size: 13.5px;
    background: linear-gradient(180deg, var(--green-light), var(--green-deep));
    border-right: 1px solid rgba(255,255,255,0.45); }
  .main-nav a.is-active { background: var(--green-active); color: #8ee59c; }
  .main-nav a.client-login { background: var(--charcoal); border: none; font-weight: 700; font-size: 14.5px; }

  .hero { position: absolute; left: 141px; top: 124px; width: 918px; height: 322px;
    background: linear-gradient(90deg, #6f7770 0%, #c9d0cc 45%, #aeb7b2 70%, #d7dcd9 100%);
    box-shadow: 0 8px 8px -4px rgba(0,0,0,0.35); }
  .hero-panel { position: absolute; left: 0; top: 48px; width: 335px; height: 227px;
    background: rgba(40,40,40,0.72); padding: 20px 20px 0 17px; color: var(--white); }
  .hero-panel h1 { color: var(--green); font-size: 35px; font-weight: 600; line-height: 1; margin-bottom: 9px; }
  .hero-panel p { font-size: 12.5px; line-height: 19px; }
  .hero-panel .learn-more { display: block; text-align: right; font-size: 11px; margin-top: 6px; color: var(--white); text-decoration: none; }

  .slider-dots { position: absolute; left: 566px; top: 467px; display: flex; gap: 7px; }
  .slider-dots span { width: 12px; height: 12px; border-radius: 50%; border: 1px solid #999; background: var(--white); }
  .slider-dots span.is-current { background: var(--charcoal); border-color: var(--charcoal); }

  .divider { position: absolute; left: 141px; top: 488px; width: 918px; height: 2px; background: var(--rule); }

  .feature { position: absolute; top: 508px; width: 289px; }
  .feature h2 { color: var(--green); font-size: 19px; font-weight: 600; line-height: 26px; height: 31px; white-space: nowrap; }
  .feature-card { height: 250px; border: 1px solid var(--card-border); }
  .feature-visual { height: 99px; }
  .feature-card p { font-size: 12.5px; line-height: 19px; padding: 9px 11px 0 12px; }
  .feature-link { display: flex; align-items: center; justify-content: space-between; margin: 2px 3px 0;
    height: 35px; padding: 0 14px 0 12px; background: var(--charcoal); color: var(--white);
    font-size: 11.5px; line-height: 14px; text-decoration: none; }
  .feature-link svg { flex: none; }

  .site-footer { position: absolute; left: 0; top: 848px; width: 1200px; height: 99px; background: var(--charcoal); color: var(--footer-text); text-align: center; }
  .social { display: flex; justify-content: center; gap: 6px; margin-top: 17px; }
  .social span { width: 20px; height: 20px; border-radius: 2px; }
  .footer-nav { margin-top: 12px; font-size: 11px; }
  .footer-nav a { color: var(--footer-text); text-decoration: none; }
  .copyright { margin-top: 6px; font-size: 10px; }
</style>
</head>
<body>
  <header class="site-header">
    <div class="brand"><span class="brand-mark"></span>Rovel Host Services LLC</div>
  </header>

  <nav class="main-nav">
    <a class="is-active" href="#" style="width:115px">Services</a>
    <a href="#" style="width:162px">Safety &amp; Security</a>
    <a href="#" style="width:225px">Data Center Specifications</a>
    <a href="#" style="width:117px">About Us</a>
    <a href="#" style="width:141px">Contact Us</a>
    <a class="client-login" href="#" style="width:157px">Client Login</a>
  </nav>

  <section class="hero" role="img" aria-label="Technician working at server racks in a data center aisle">
    <div class="hero-panel">
      <h1>Why Rovel</h1>
      <p>You need safe, always-on data, and you need unwavering confidence in the partner you choose to manage it. With a potent combination of upscale technological sophistication and down-home trustworthy service, Rovel is the reliable, user-friendly data center solution your growing business demands.</p>
      <a class="learn-more" href="#">Learn More</a>
    </div>
  </section>

  <div class="slider-dots"><span class="is-current"></span><span></span><span></span><span></span></div>
  <div class="divider"></div>

  <article class="feature" style="left:141px">
    <h2>Safe, Secure, Invisible</h2>
    <div class="feature-card">
      <div class="feature-visual" role="img" aria-label="Padlock on a blue circuit board" style="background:radial-gradient(circle at 45% 50%, #5aa0e8, #1a3f9a 70%)"></div>
      <p>Thieves can't steal it if they don't know it's there, which is why the Rovel Data Center facility is built to be invisible. And even if they stumble across us, they have to get in – and back out – to pose a threat to your data. Rovel's commitment to security best practices ensure that this threat is nullified.</p>
    </div>
    <a class="feature-link" href="#">Tour The Most Secure Data Facility In Texas <svg width="8" height="10"><polygon points="0,0 8,5 0,10" fill="#fff"/></svg></a>
  </article>

  <article class="feature" style="left:456px">
    <h2>Lower Total Cost of Ownership</h2>
    <div class="feature-card">
      <div class="feature-visual" role="img" aria-label="Cycle diagram centred on lower TCO" style="background:radial-gradient(circle at 50% 50%, #e4e4e4 0, #c8c8c8 45px, #fff 47px)"></div>
      <p>The appeal of outsourcing is that it strengthens your cash flow while freeing your company's decision makers from the minutiae of IT management. Rovel's revolutionary design features help maximize the financial rewards of outsourcing, both now and over the long term.</p>
    </div>
    <a class="feature-link" href="#">How Data Outsourcing Can Strengthen<br>Your Bottom Line <svg width="8" height="10"><polygon points="0,0 8,5 0,10" fill="#fff"/></svg></a>
  </article>

  <article class="feature" style="left:770px">
    <h2>Business Continuity</h2>
    <div class="feature-card">
      <div class="feature-visual" role="img" aria-label="Two silhouetted businessmen shaking hands in a server aisle" style="background:linear-gradient(90deg, #1f5a66, #7fb8c0 50%, #2a6470)"></div>
      <p>If the biggest known threat to data security were sand, would you store your data on the beach? Neither would we. That's why we chose the mild climate and stable meteorological conditions of San Antonio to securely house your data in.</p>
    </div>
    <a class="feature-link" href="#">See How Security Begins At (Our) Home <svg width="8" height="10"><polygon points="0,0 8,5 0,10" fill="#fff"/></svg></a>
  </article>

  <footer class="site-footer">
    <div class="social">
      <span style="background:#4a90d9"></span><span style="background:#3b5998"></span><span style="background:#3fa9e0"></span><span style="background:#1f6fa8"></span><span style="background:#f08a24"></span>
    </div>
    <div class="footer-nav"><a href="#">Home</a> | <a href="#">Services</a> | <a href="#">Safety &amp; Security</a> | <a href="#">Data Center Specifications</a> | <a href="#">About Us</a> | <a href="#">Contact Us</a></div>
    <div class="copyright">Copyright 2010 Rovel Host Services, All Rights Reserved.</div>
  </footer>
</body>
</html>
```